Front cover for our tenth anniversary show programme

To create an eye catching tenth anniversary front cover for our programme

Moonbrook presents DANCE! 2015

date of the show Sunday 3rd May 2015

Venue The Harrowgate Stagehouse

please see the updated brief!

Reason: there hasn't been anything that is quite right

```html
<!DOCTYPE html>
<html lang="en">
<head>
<meta charset="utf-8">
<title>Moonbrook presents DANCE! 2015 – Programme Cover</title>
<link rel="stylesheet" href="https://fonts.googleapis.com/css2?family=Marcellus+SC&family=Roboto:wght@400;500&family=Cormorant+Garamond:ital,wght@1,600&display=swap">
<style>
  :root {
    --page-bg: #a87d55;
    --cover-black: #0b0a0b;
    --cover-grey: #2e2c2d;
    --pink: #ec5fa6;
    --pink-deep: #c42a7a;
    --silver-light: #e9e9ea;
    --silver-dark: #8b8c8f;
    --plum: #5a2744;
    --plum-dark: #2a1220;
    --photo-magenta: #a0184f;
    --photo-dark: #1a0710;
    --text-light: #f4f1ee;
  }
  * { margin: 0; padding: 0; box-sizing: border-box; }
  html, body {
    width: 917px;
    height: 1200px;
    overflow: hidden;
    background: var(--page-bg);
  }
  .cover {
    position: absolute;
    left: 34px;
    top: 0;
    width: 848px;
    height: 1200px;
    background:
      radial-gradient(ellipse at 70% 30%, var(--cover-grey) 0%, var(--cover-black) 60%),
      var(--cover-black);
    overflow: hidden;
  }
  .cover-art {
    position: absolute;
    inset: 0;
    width: 100%;
    height: 100%;
  }
  .badge-name {
    position: absolute;
    left: 137px;
    top: 300px;
    width: 256px;
    text-align: center;
    font-family: "Roboto", sans-serif;
    font-weight: 500;
    font-size: 46px;
    color: var(--text-light);
    letter-spacing: 1px;
  }
  .badge-tagline {
    position: absolute;
    left: 137px;
    top: 362px;
    width: 256px;
    text-align: center;
    font-family: "Roboto", sans-serif;
    font-weight: 500;
    font-size: 18px;
    line-height: 1.25;
    color: var(--text-light);
  }
  .badge-tagline .years {
    display: block;
    font-size: 32px;
    color: var(--pink);
  }
  .show-title {
    position: absolute;
    left: 510px;
    top: 130px;
    width: 290px;
    text-align: center;
    font-family: "Marcellus SC", serif;
    font-size: 48px;
    line-height: 66px;
    color: var(--text-light);
  }
  .show-details {
    position: absolute;
    left: 58px;
    top: 1062px;
    color: var(--text-light);
    font-family: "Roboto", sans-serif;
  }
  .show-date {
    font-size: 24px;
    font-weight: 400;
    margin-bottom: 10px;
  }
  .show-venue {
    font-size: 28px;
    font-weight: 500;
  }
  .venue-label {
    font-family: "Cormorant Garamond", serif;
    font-style: italic;
    font-weight: 600;
    font-size: 30px;
    margin-right: 6px;
  }
</style>
</head>
<body>
  <main class="cover">
    <svg class="cover-art" viewBox="0 0 528 747" preserveAspectRatio="none" aria-hidden="false">
      <defs>
        <linearGradient id="photoTone" x1="0" y1="0" x2="1" y2="1">
          <stop offset="0" stop-color="var(--photo-dark)"/>
          <stop offset="0.45" stop-color="var(--photo-magenta)"/>
          <stop offset="1" stop-color="var(--photo-dark)"/>
        </linearGradient>
        <linearGradient id="silver" x1="0" y1="0" x2="0" y2="1">
          <stop offset="0" stop-color="var(--silver-light)"/>
          <stop offset="1" stop-color="var(--silver-dark)"/>
        </linearGradient>
        <radialGradient id="badgeFill" cx="0.5" cy="0.45" r="0.6">
          <stop offset="0" stop-color="var(--plum)"/>
          <stop offset="1" stop-color="var(--plum-dark)"/>
        </radialGradient>
      </defs>

      <!-- dancers photograph area -->
      <path class="photo-area" role="img" aria-label="Photograph of young dancers in black leotards performing under pink stage lighting"
        d="M0,335 C120,300 220,310 300,335 S450,358 528,348 L528,575 C480,585 430,622 360,622 C250,625 120,555 0,560 Z"
        fill="url(#photoTone)"/>

      <!-- upper wave bands -->
      <path class="band-pink" d="M0,327 C120,292 220,302 300,327 S450,350 528,340 L528,348 C450,358 380,345 300,335 C220,310 120,300 0,335 Z" fill="var(--pink)"/>
      <path class="band-silver" d="M0,335 C120,300 220,310 300,335 S450,358 528,348 L528,354 C450,364 380,351 300,341 C220,316 120,306 0,340 Z" fill="url(#silver)"/>

      <!-- lower wave bands -->
      <path class="band-pink" d="M0,553 C120,548 250,618 360,615 S480,578 528,568 L528,575 C480,585 430,622 360,622 C250,625 120,555 0,560 Z" fill="var(--pink)"/>
      <path class="band-silver" d="M0,560 C120,555 250,625 360,622 S480,585 528,575 L528,581 C480,591 430,628 360,628 C250,631 120,561 0,566 Z" fill="url(#silver)"/>

      <!-- anniversary badge -->
      <circle class="badge" cx="165" cy="217" r="100" fill="url(#badgeFill)" stroke="var(--pink)" stroke-width="5"/>
    </svg>

    <div class="badge-name">Moonbrook</div>
    <div class="badge-tagline">Celebrating<span class="years">Ten Years</span></div>

    <h1 class="show-title">Moonbrook<br>Presents<br>DANCE!<br>2015</h1>

    <section class="show-details">
      <p class="show-date">Sunday 3rd May 2015</p>
      <p class="show-venue"><span class="venue-label">Venue:</span>The Harrowgate Stagehouse</p>
    </section>
  </main>
</body>
</html>
```